Business Card Design Project

Business card design based on the existing logo.

Target Market(s)

Small to medium business owners and CIO's looking for professional IT services.

Industry/Entity Type

Business

Font styles to use
Serif
Sans Serif

Requirements
Must have
• Logo, company name, company details

Text to appear on the business card
Name / Title:
Leon Fairholt
CEO

Address:
Valtiro Limited
Level 3, 42 Kestle St
P O Box 462
Paraparaumu 5391

Other details:
leon@valtiro.co
Ph: 0800 519 308
Mob: +64 21 948 216
www.valtiro.co

Nice to have
• I would look at both single and double sided options. My initial thought is double sided with just the logo with the grey framing for the front and the name and details on the back. But I'm open to other design options.

```html
<!DOCTYPE html>
<html lang="en">
<head>
<meta charset="utf-8">
<title>Valtiro Limited – Business Card</title>
<link rel="stylesheet" href="https://fonts.googleapis.com/css2?family=Open+Sans:wght@400;600&display=swap">
<style>
  :root {
    --backdrop: #1b1c1d;
    --brand-blue: #6fa6d0;
    --card-white: #ffffff;
    --text-grey: #8a8a8a;
    --rule-grey: #b9c7d3;
  }
  * { box-sizing: border-box; margin: 0; padding: 0; }
  html, body {
    width: 1200px; height: 1000px; overflow: hidden;
    background: var(--backdrop);
    font-family: "Open Sans", Arial, sans-serif;
  }
  .canvas { position: relative; width: 1200px; height: 1000px; }

  /* Front of card */
  .card-front {
    position: absolute; left: 90px; top: 358px;
    width: 552px; height: 285px;
    background: var(--brand-blue);
    display: flex; align-items: center; justify-content: center; gap: 18px;
  }
  .card-front .brand-mark {
    width: 46px; height: 46px; border-radius: 50%;
    background: var(--card-white);
  }
  .card-front .brand-name {
    color: var(--card-white);
    font-size: 72px; font-weight: 400; letter-spacing: 1px; line-height: 1;
  }

  /* Back of card */
  .card-back {
    position: absolute; left: 760px; top: 224px;
    width: 285px; height: 552px;
    background: var(--card-white);
    border-left: 15px solid var(--brand-blue);
    padding: 44px 26px 0 22px;
  }
  .card-back .brand-name {
    color: var(--brand-blue);
    font-size: 46px; font-weight: 400; line-height: 1;
    text-align: right;
  }
  .person { margin-top: 78px; }
  .person .name { color: var(--brand-blue); font-size: 21px; line-height: 1.2; }
  .person .role { color: var(--text-grey); font-size: 21px; line-height: 1.15; }

  .address { margin-top: 34px; }
  .label {
    color: var(--brand-blue); font-size: 12px; letter-spacing: 0.5px;
    text-transform: uppercase;
  }
  .address p { color: var(--text-grey); font-size: 14px; line-height: 1.32; }

  .contacts {
    position: absolute; left: 22px; bottom: 46px;
    display: grid; grid-template-columns: 20px 1fr; column-gap: 10px;
  }
  .contacts .icons {
    display: flex; flex-direction: column; justify-content: space-around;
    border-right: 1px solid var(--rule-grey); padding-right: 6px;
  }
  .contacts .icons svg { width: 11px; height: 11px; display: block; }
  .contacts ul { list-style: none; }
  .contacts li { color: var(--text-grey); font-size: 14px; line-height: 1.45; }
</style>
</head>
<body>
<main class="canvas">

  <section class="card-front" aria-label="Card front">
    <span class="brand-mark"></span>
    <span class="brand-name">Valtiro</span>
  </section>

  <section class="card-back" aria-label="Card back">
    <div class="brand-name">Valtiro</div>

    <div class="person">
      <p class="name">Leon Fairholt</p>
      <p class="role">CEO</p>
    </div>

    <div class="address">
      <p class="label">Address</p>
      <p>Valtiro Limited<br>Level 3, 42 Kestle St<br>P O Box 462<br>Paraparaumu 5391</p>
    </div>

    <div class="contacts">
      <div class="icons">
        <svg viewBox="0 0 12 12" aria-hidden="true"><rect x="3" y="0.5" width="6" height="11" rx="1" fill="none" stroke="#6fa6d0"/><line x1="5" y1="9.5" x2="7" y2="9.5" stroke="#6fa6d0"/></svg>
        <svg viewBox="0 0 12 12" aria-hidden="true"><path d="M2.5 1 L4.5 1 L5.3 3.6 L4 4.6 Q5 7 7.4 8 L8.4 6.7 L11 7.5 L11 9.5 Q6.5 11 3 7 Q0.8 4 2.5 1 Z" fill="#6fa6d0"/></svg>
        <svg viewBox="0 0 12 12" aria-hidden="true"><rect x="0.5" y="2.5" width="11" height="7" fill="none" stroke="#6fa6d0"/><path d="M0.5 2.5 L6 7 L11.5 2.5" fill="none" stroke="#6fa6d0"/></svg>
        <svg viewBox="0 0 12 12" aria-hidden="true"><circle cx="6" cy="6" r="5.5" fill="none" stroke="#6fa6d0"/><ellipse cx="6" cy="6" rx="2.4" ry="5.5" fill="none" stroke="#6fa6d0"/><line x1="0.5" y1="6" x2="11.5" y2="6" stroke="#6fa6d0"/></svg>
      </div>
      <ul>
        <li>0800 519 308</li>
        <li>+64 21 948 216</li>
        <li>leon@valtiro.co</li>
        <li>www.valtiro.co</li>
      </ul>
    </div>
  </section>

</main>
</body>
</html>
```